Professional/Sleek card design for athletic apparel brand

Athletic apparel brand. Mainly focused on lifting weights/gym workouts. Logo and brand are already created. Must use brand logo and name. Creativity is welcome. Looking for a clean, modern, and sexy design.

```html
<!DOCTYPE html>
<html lang="en">
<head>
<meta charset="utf-8">
<title>Iron and Grit – Business Card</title>
<link rel="stylesheet" href="https://fonts.googleapis.com/css2?family=Open+Sans:wght@400;600;700&display=swap">
<style>
  :root {
    --stage: #e9e9eb;
    --ink: #0b0b0c;
    --paper: #ffffff;
    --pattern-light: #2a2a2d;
    --pattern-dark: #0d0d0f;
    --muted: #1e1e20;
  }
  html, body {
    margin: 0;
    width: 1200px;
    height: 780px;
    overflow: hidden;
    background: var(--stage);
  }
  .canvas {
    position: relative;
    width: 1200px;
    height: 780px;
    display: flex;
    align-items: center;
    justify-content: center;
    gap: 40px;
  }
  .card {
    width: 560px;
    height: 320px;
    box-shadow: 0 10px 30px rgba(0,0,0,0.25);
  }
  .card svg { display: block; }
  .brand-text {
    font-family: "Open Sans", sans-serif;
    font-weight: 600;
  }
  .brand-text--front {
    font-size: 17px;
    letter-spacing: 9px;
    fill: var(--ink);
  }
  .brand-text--back {
    font-size: 8px;
    letter-spacing: 2px;
    fill: var(--paper);
  }
  .person-name {
    font-family: "Open Sans", sans-serif;
    font-weight: 700;
    font-size: 28px;
    fill: var(--ink);
  }
  .person-title {
    font-family: "Open Sans", sans-serif;
    font-weight: 400;
    font-size: 15px;
    fill: var(--ink);
  }
  .contact-text {
    font-family: "Open Sans", sans-serif;
    font-weight: 400;
    font-size: 13px;
    fill: var(--ink);
  }
  .address-text {
    font-family: "Open Sans", sans-serif;
    font-weight: 600;
    font-size: 12.5px;
    fill: var(--paper);
  }
</style>
</head>
<body>
<main class="canvas">

  <section class="card card-back" aria-label="Card back">
    <svg width="560" height="320" viewBox="0 0 560 320">
      <defs>
        <linearGradient id="patternTone" x1="0" y1="0" x2="1" y2="1">
          <stop offset="0" stop-color="var(--pattern-light)"/>
          <stop offset="0.55" stop-color="var(--pattern-dark)"/>
          <stop offset="1" stop-color="var(--muted)"/>
        </linearGradient>
      </defs>
      <rect class="back-pattern" width="560" height="320" fill="url(#patternTone)" role="img" aria-label="Repeating brand-mark pattern in glossy black on black"/>
      <g class="back-stamp">
        <circle cx="466" cy="287" r="4" fill="var(--paper)"/>
        <text class="brand-text brand-text--back" x="538" y="290" text-anchor="end">IRON AND GRIT</text>
      </g>
    </svg>
  </section>

  <section class="card card-front" aria-label="Card front">
    <svg width="560" height="320" viewBox="0 0 560 320">
      <rect class="front-paper" width="560" height="320" fill="var(--paper)"/>
      <path class="front-band" d="M0,320 L0,305 Q420,302 560,172 L560,320 Z" fill="var(--ink)"/>
      <path class="front-swoosh" d="M40,296 Q420,288 545,150" fill="none" stroke="var(--ink)" stroke-width="3" stroke-linecap="round"/>

      <g class="brand-lockup">
        <circle cx="152" cy="56" r="7" fill="var(--ink)"/>
        <text class="brand-text brand-text--front" x="170" y="62">IRON AND GRIT</text>
      </g>

      <g class="identity">
        <text class="person-name" x="30" y="156">Marta Kovalenko</text>
        <text class="person-title" x="32" y="178">Managing Director</text>
      </g>

      <line class="divider" x1="270" y1="104" x2="270" y2="192" stroke="var(--ink)" stroke-width="1.5"/>

      <g class="contacts">
        <rect x="286" y="108" width="7" height="12" rx="1.5" fill="none" stroke="var(--ink)" stroke-width="1.5"/>
        <text class="contact-text" x="302" y="119">(555) 014-2290</text>

        <path d="M284,135 q6,-6 12,0 l-1.5,2 h-9 z M286,137 h8 v5 h-8 z" fill="var(--ink)"/>
        <text class="contact-text" x="302" y="142">(555) 014-2290</text>

        <rect x="284" y="156" width="12" height="9" fill="none" stroke="var(--ink)" stroke-width="1.5"/>
        <path d="M284,156 l6,5 l6,-5" fill="none" stroke="var(--ink)" stroke-width="1.2"/>
        <text class="contact-text" x="302" y="165">info@ironandgrit.example</text>

        <circle cx="290" cy="184" r="6" fill="none" stroke="var(--ink)" stroke-width="1.5"/>
        <path d="M284,184 h12 M290,178 q-4,6 0,12 q4,-6 0,-12" fill="none" stroke="var(--ink)" stroke-width="1"/>
        <text class="contact-text" x="302" y="188">www.ironandgrit.example</text>
      </g>

      <text class="address-text" x="540" y="308" text-anchor="end">1820 Ridgeway Blvd. Suite 140 Fort Worth, TX 76104</text>
    </svg>
  </section>

</main>
</body>
</html>
```